6x9 Postcard Design Project

I have a web design and marketing company. I need a 6x9 postcard designed that grabs attention and tells all my services.

I have launched a new "Website Leasing" plan that allows small businesses to have a professionally designed website for an small down and a monthly payment. I want one side of the card to be about the leasing plan and its pricing.

I would also like all my services included.

Web Design
Search Engine Optimization
Social Media Services
Graphic Design
Video Production
IT Services
Low Monthly Pricing!

For more information about the leasing plan and all my services please use the content on:

www.plumvexo.com

I would like the design to follow my website color scheme BUT NOT THAT SAME LOOK AS MY WEBSITE, I am looking for creativity. I am open to other colors as well. Again, please do not make the design look like my website, I need something I can't do.

The final design files should also have a PSD so I can edit it as my services and prices change.

The final design should present my company as a professional, current and savvy design firm.

I am located in Mesa, Arizona
I serve Phoenix, Mesa, Gilbert, Chandler and all of Arizona.

Marcus
480-555-0173
Updates

This will be mailed out so it will need the appropriate area for the post office info

Hello,

I uploaded two templates that show the post office guidelines in regards to where the the ink free areas need to go. Thanks,

Marcus

Target Market(s)

Small/Medium Businesses

Industry/Entity Type

Graphic Design

Requirements
Must have
• Must have a place for the post office mailing info.
Nice to have
• A unique design that does not emulate my current website
Should not have
• It should not look like my website. I need a postcard design that is unique and not a clone of my site.

```html
<!DOCTYPE html>
<html lang="en">
<head>
<meta charset="utf-8">
<title>Plumvexo Website Leasing Postcard</title>
<link href="https://fonts.googleapis.com/css2?family=Roboto+Condensed:wght@400;700&display=swap" rel="stylesheet">
<style>
  :root {
    --page: #e6e6e4;
    --white: #ffffff;
    --blue: #2e9bd3;
    --blue-deep: #1f86c2;
    --blue-light: #8ccbec;
    --green: #5cb845;
    --green-bright: #74c842;
    --green-pale: #d9f0c8;
    --text-blue: #1e8bcc;
    --text-green: #4db53a;
    --logo-grey: #5b5f63;
  }
  * { box-sizing: border-box; margin: 0; padding: 0; }
  html, body { width: 1200px; height: 800px; overflow: hidden; }
  body {
    background: var(--page);
    font-family: "Roboto Condensed", "Arial Narrow", sans-serif;
    position: relative;
  }
  .card {
    position: absolute;
    width: 570px;
    height: 380px;
    background: var(--white);
    overflow: hidden;
  }
  .card--mailing { left: 20px; top: 210px; }
  .card--offer { left: 610px; top: 210px; }

  /* mailing side */
  .mailing__top-band {
    position: absolute; left: 0; top: 0;
    width: 262px; height: 62px;
    background: var(--blue);
  }
  .mailing__bottom-band {
    position: absolute; left: 0; bottom: 0;
    width: 100%; height: 46px;
    background: linear-gradient(to bottom, var(--blue-light) 0 22%, var(--blue) 22% 100%);
  }
  .mailing__swirl {
    position: absolute; left: 0; top: 205px;
    width: 190px; height: 150px;
  }
  .offer-text {
    position: absolute;
    text-align: center;
    font-weight: 700;
    color: var(--text-blue);
    line-height: 1.12;
  }
  .offer-text .price { color: var(--text-green); }
  .offer-text .without { color: var(--text-green); }
  .mailing__offer {
    left: 48px; top: 243px; width: 120px;
    font-size: 9.5px;
  }
  .mailing__offer .price { font-size: 12.5px; }
  .mailing__offer .without { font-size: 12.5px; }
  .brand {
    position: absolute;
    display: flex; align-items: center; gap: 5px;
    font-weight: 700;
    color: var(--logo-grey);
    letter-spacing: -0.5px;
  }
  .brand__dot { border-radius: 50%; background: var(--green); }
  .mailing__brand { left: 192px; top: 302px; font-size: 26px; }
  .mailing__brand .brand__dot { width: 9px; height: 9px; }

  /* offer side */
  .offer__photo {
    position: absolute; left: 0; top: 0;
    width: 360px; height: 330px;
    background: linear-gradient(to right, #cfc7bf 0%, #e2dcd4 35%, #bcd6d3 70%, rgba(130,196,110,0) 100%);
  }
  .offer__green {
    position: absolute; left: 0; top: 0;
    width: 100%; height: 330px;
    background: linear-gradient(to right, rgba(92,184,69,0) 40%, var(--green) 70%, var(--green-bright) 100%);
  }
  .offer__footer {
    position: absolute; left: 0; bottom: 0;
    width: 100%; height: 80px;
  }
  .offer__services {
    position: absolute; left: 0; top: 318px;
    width: 322px; height: 38px;
    background: var(--blue);
    clip-path: polygon(0 0, 100% 0, 95% 100%, 0 100%);
    color: var(--white);
    font-weight: 700;
    font-size: 9.6px;
    line-height: 1.35;
    padding: 4px 0 0 7px;
  }
  .offer__circle {
    position: absolute; left: 318px; top: 30px;
    width: 256px; height: 256px;
  }
  .offer__text {
    left: 360px; top: 84px; width: 172px;
    font-size: 15px;
  }
  .offer__text .price { font-size: 19px; }
  .offer__text .without { font-size: 20px; }
  .offer__brand { left: 352px; top: 328px; font-size: 36px; }
  .offer__brand .brand__dot { width: 11px; height: 11px; }
</style>
</head>
<body>

<section class="card card--mailing" aria-label="Postcard mailing side">
  <div class="mailing__top-band"></div>
  <svg class="mailing__swirl" viewBox="0 0 190 150" aria-hidden="true">
    <circle cx="90" cy="80" r="72" fill="none" stroke="#d6ecf8" stroke-width="10"/>
    <path d="M 25 115 A 72 72 0 1 1 120 146" fill="none" stroke="#2e9bd3" stroke-width="6" stroke-linecap="round"/>
    <path d="M 40 60 A 55 55 0 0 1 140 60" fill="none" stroke="#8ccbec" stroke-width="3"/>
  </svg>
  <p class="offer-text mailing__offer">
    For Only<br>
    <span class="price">$249.00</span> monthly.<br>
    You Can have a Current &amp;<br>
    Marketable Website<br>
    <span class="without">Without</span><br>
    the Lump Sum<br>
    Headache.
  </p>
  <div class="brand mailing__brand"><span>Plumvexo</span><span class="brand__dot"></span></div>
  <div class="mailing__bottom-band"></div>
</section>

<section class="card card--offer" aria-label="Postcard offer side">
  <div class="offer__photo" role="img" aria-label="Photo of a surprised woman shopping beside a clothing rack"></div>
  <div class="offer__green"></div>
  <svg class="offer__footer" viewBox="0 0 570 80" preserveAspectRatio="none" aria-hidden="true">
    <path d="M0 20 L300 20 Q420 0 570 -4 L570 80 L0 80 Z" fill="#ffffff"/>
  </svg>
  <svg class="offer__circle" viewBox="0 0 256 256" aria-hidden="true">
    <defs>
      <radialGradient id="offerGlow" cx="50%" cy="50%" r="50%">
        <stop offset="0%" stop-color="#ffffff"/>
        <stop offset="55%" stop-color="#f2faec"/>
        <stop offset="85%" stop-color="#9fd982"/>
        <stop offset="100%" stop-color="#5cb845"/>
      </radialGradient>
    </defs>
    <circle cx="128" cy="128" r="124" fill="#4fa83b"/>
    <circle cx="132" cy="126" r="112" fill="url(#offerGlow)"/>
  </svg>
  <p class="offer-text offer__text">
    For Only<br>
    <span class="price">$249.00</span> monthly.<br>
    You Can have a Current &amp;<br>
    Marketable Website<br>
    <span class="without">Without</span><br>
    the Lump Sum<br>
    Headache.
  </p>
  <div class="offer__services">
    Web Design | Search Engine Optimization | Social Media Services |<br>
    Graphic Design | Video Production | IT Services | Low Monthly Pricing
  </div>
  <div class="brand offer__brand"><span>Plumvexo</span><span class="brand__dot"></span></div>
</section>

</body>
</html>
```